Below Par Parenting

I would like a poster (size to be agreed) created for the wording that I have composed and which I have pasted below. The poster is for my own personal gratification. It is not for commercial use. The message is driven by honesty and a profound sense of mea culpa. I am open to ideas regarding style and presentation.
I am an awful parent. No question. I am not cut out for this shit. I’m too quick to temper. I turn everything into a test of wills. I’m not down for food on the floor, for having my car trashed with your stink and detritus, for having the walls of my house daubed in your greasy fingerprints. I want to listen to The Marrows not Up the Paper Ladder on repeat. I enjoyed making you but, on reflection, I should have pulled out. Let me go back in time to that great waste of space and energy that is ante-natal classes and tell that boho with the flowery dress and curly hair, ‘Why are you concentrating on the first five seconds? All the pain comes later. Why aren’t you telling us what to do when they won’t sleep, when they won’t sit in their high chairs, when they won’t sleep on the aeroplane?’ Boy, I wish I could play it loosey-goosey like those left-leaning parents I see going ‘coo-coo’ in Benvolti’s but I’m not built like that. I am a right-wing despot. It’s Nazi Germany back at my place. I’m not interested in your meltdowns and tantrums. You want to writhe on the floor in the car park going red in the face? Make my day. You want to go spastic because I won’t let you watch TV for five hours straight? I don’t give a shit. Read my lips. I won’t pander to it. My wife says you’re babies but all I see is little people with an agenda. I’ve got naughty steps and sin-bins all over the joint. I wish I wasn’t the tyrant, the Valdarrez and the Okoro Tembe I am but it is what it is. I blame my parents and they, in turn, will blame me and their parents. Understand I don’t want to infect you too much with my bad behavior but if you could stop making such a scene in public places with your screaming, your bitching and your all round refusal to play nice then maybe, just maybe, we’d have a chance and I wouldn’t be such an awful parent.

```html
<!DOCTYPE html>
<html lang="en">
<head>
<meta charset="utf-8">
<title>Below Par Parenting</title>
<link rel="stylesheet" href="https://fonts.googleapis.com/css2?family=Inter+Tight:wght@700&display=swap">
<style>
  :root {
    --poster-ground: #000000;
    --poster-ink: #ffffff;
  }
  html, body {
    margin: 0;
    padding: 0;
    width: 853px;
    height: 1200px;
    overflow: hidden;
    background: var(--poster-ground);
  }
  .poster {
    display: block;
    width: 853px;
    height: 1200px;
    background: var(--poster-ground);
  }
  .manifesto-line {
    fill: var(--poster-ink);
    font-family: "Inter Tight", "Helvetica Neue", Arial, sans-serif;
    font-weight: 700;
    text-transform: uppercase;
  }
</style>
</head>
<body>
<svg class="poster" viewBox="0 0 853 1200" width="853" height="1200" xmlns="http://www.w3.org/2000/svg" role="img" aria-label="Below Par Parenting manifesto">
  <rect class="poster-ground" width="853" height="1200" fill="var(--poster-ground)"/>
  <g class="manifesto">
    <text class="manifesto-line" x="85" y="103" font-size="53" textLength="683" lengthAdjust="spacingAndGlyphs">I am an awful parent.</text>
    <text class="manifesto-line" x="85" y="160" font-size="69" textLength="683" lengthAdjust="spacingAndGlyphs">No question.</text>
    <text class="manifesto-line" x="85" y="195" font-size="40" textLength="683" lengthAdjust="spacingAndGlyphs">I am not cut out for this shit.</text>
    <text class="manifesto-line" x="85" y="234" font-size="48" textLength="683" lengthAdjust="spacingAndGlyphs">I’m too quick to temper,</text>
    <text class="manifesto-line" x="85" y="272" font-size="43" textLength="683" lengthAdjust="spacingAndGlyphs">too ready to go Nagasaki.</text>
    <text class="manifesto-line" x="85" y="293" font-size="17" textLength="683" lengthAdjust="spacingAndGlyphs">I’m not down for food on the floor, for having my car</text>
    <text class="manifesto-line" x="85" y="311" font-size="17" textLength="683" lengthAdjust="spacingAndGlyphs">smeared with your stink and detritus, for having the walls</text>
    <text class="manifesto-line" x="85" y="330" font-size="17" textLength="683" lengthAdjust="spacingAndGlyphs">of my house daubed in your bolognaise fingerprints.</text>
    <text class="manifesto-line" x="85" y="364" font-size="38" textLength="683" lengthAdjust="spacingAndGlyphs">I want to listen to Hollow Lanterns</text>
    <text class="manifesto-line" x="85" y="397" font-size="37" textLength="683" lengthAdjust="spacingAndGlyphs">not Up the Paper Ladder on repeat.</text>
    <text class="manifesto-line" x="85" y="429" font-size="35" textLength="683" lengthAdjust="spacingAndGlyphs">I enjoyed making you but on reflection</text>
    <text class="manifesto-line" x="85" y="470" font-size="48" textLength="683" lengthAdjust="spacingAndGlyphs">I should have pulled out.</text>
    <text class="manifesto-line" x="85" y="487" font-size="14" textLength="683" lengthAdjust="spacingAndGlyphs">Let me go back in time to that great waste of space and energy that</text>
    <text class="manifesto-line" x="85" y="502" font-size="14" textLength="683" lengthAdjust="spacingAndGlyphs">was ante-natal classes and tell that boho with the flowery dress,</text>
    <text class="manifesto-line" x="85" y="531" font-size="31" textLength="683" lengthAdjust="spacingAndGlyphs">‘Why are you concentrating on the labour?</text>
    <text class="manifesto-line" x="85" y="566" font-size="38" textLength="683" lengthAdjust="spacingAndGlyphs">All the hard work comes later.’</text>
    <text class="manifesto-line" x="85" y="585" font-size="15" textLength="683" lengthAdjust="spacingAndGlyphs">Boy, I wish I could play it loosey-goosey like those left-leaning</text>
    <text class="manifesto-line" x="85" y="603" font-size="15" textLength="683" lengthAdjust="spacingAndGlyphs">parents I see going ‘coo-coo’ in Benvolti’s but I’m not built like that.</text>
    <text class="manifesto-line" x="85" y="647" font-size="48" textLength="683" lengthAdjust="spacingAndGlyphs">I am a right-wing despot.</text>
    <text class="manifesto-line" x="85" y="696" font-size="60" textLength="683" lengthAdjust="spacingAndGlyphs">It’s Guantanamo Bay</text>
    <text class="manifesto-line" x="85" y="714" font-size="15" textLength="683" lengthAdjust="spacingAndGlyphs">back at my place; no rights of reply, no naughty-steps just sin bins.</text>
    <text class="manifesto-line" x="85" y="754" font-size="47" textLength="683" lengthAdjust="spacingAndGlyphs">I’m not interested in your</text>
    <text class="manifesto-line" x="85" y="794" font-size="47" textLength="683" lengthAdjust="spacingAndGlyphs">meltdowns and tantrums.</text>
    <text class="manifesto-line" x="85" y="813" font-size="18" textLength="683" lengthAdjust="spacingAndGlyphs">You want to writhe on the floor in the car park going red</text>
    <text class="manifesto-line" x="85" y="832" font-size="18" textLength="683" lengthAdjust="spacingAndGlyphs">in the face? Make my day. You want to go spastic because I</text>
    <text class="manifesto-line" x="85" y="851" font-size="18" textLength="683" lengthAdjust="spacingAndGlyphs">won’t let you watch TV for five hours straight?</text>
    <text class="manifesto-line" x="85" y="873" font-size="22" textLength="683" lengthAdjust="spacingAndGlyphs">I don’t give a shit. Read my lips. I won’t pander to it.</text>
    <text class="manifesto-line" x="85" y="887" font-size="10" textLength="683" lengthAdjust="spacingAndGlyphs">My wife says you’re babies but all I see is little people with an agenda and their own language. What is it that you speak? Hutu with Hebrew?</text>
    <text class="manifesto-line" x="85" y="913" font-size="29" textLength="683" lengthAdjust="spacingAndGlyphs">Damn, I wish I wasn’t the tyrant, the Valdarrez</text>
    <text class="manifesto-line" x="85" y="942" font-size="33" textLength="683" lengthAdjust="spacingAndGlyphs">and the Okoro Tembe I am but it is what it is.</text>
    <text class="manifesto-line" x="85" y="963" font-size="21" textLength="683" lengthAdjust="spacingAndGlyphs">But who am I kidding? You don’t respect me or my mortgage.</text>
    <text class="manifesto-line" x="85" y="980" font-size="15" textLength="683" lengthAdjust="spacingAndGlyphs">I can’t pooh in the bath like you do. (I pee but that’s not the same) you’re up</text>
    <text class="manifesto-line" x="85" y="997" font-size="15" textLength="683" lengthAdjust="spacingAndGlyphs">there with Rory Flint leaving your bedroom looking like the Tet Offensive.</text>
    <text class="manifesto-line" x="85" y="1026" font-size="31" textLength="683" lengthAdjust="spacingAndGlyphs">I give up. I sue for peace. Halloran style.</text>
    <text class="manifesto-line" x="85" y="1046" font-size="17" textLength="683" lengthAdjust="spacingAndGlyphs">I’ll be downstairs beaten with a whisky. Do as you please. I can’t control you</text>
    <text class="manifesto-line" x="85" y="1076" font-size="33" textLength="683" lengthAdjust="spacingAndGlyphs">but know that I’m here if you need me.</text>
  </g>
</svg>
</body>
</html>
```